Pinecrest Lockworks Business Card Design

Double Sided Business Card Design for a Locksmith company specializing in Safecracking, safe & vault service.

```html
<!DOCTYPE html>
<html lang="en">
<head>
<meta charset="utf-8">
<title>Pinecrest Lockworks Business Card</title>
<link href="https://fonts.googleapis.com/css2?family=Source+Sans+3:wght@400;600;700;800&display=swap" rel="stylesheet">
<style>
  :root {
    --canvas: #e4e4e4;
    --card: #070808;
    --green: #1e7a3c;
    --green-deep: #15562a;
    --white: #ffffff;
    --rule: #d8d8d8;
  }
  * { margin: 0; padding: 0; box-sizing: border-box; }
  html, body { width: 1200px; height: 960px; overflow: hidden; }
  body {
    background: var(--canvas);
    font-family: "Source Sans 3", Arial, sans-serif;
    color: var(--white);
    position: relative;
  }
  .card {
    position: absolute;
    left: 305px;
    width: 597px;
    height: 341px;
    background: var(--card);
    overflow: hidden;
  }
  .card--front { top: 119px; }
  .card--back { top: 513px; }

  /* Front */
  .front-art {
    position: absolute;
    left: 553px;
    top: 0;
    width: 44px;
    height: 341px;
  }
  .front-art {
    left: 555px;
    width: 347px;
  }
  .front-art-fill {
    position: absolute;
    left: 250px;
    top: 0;
    width: 347px;
    height: 341px;
    background: linear-gradient(160deg, var(--green) 0%, var(--green-deep) 55%, var(--card) 100%);
  }
  .front-brand {
    position: absolute;
    left: 45px;
    top: 224px;
    font-weight: 800;
    font-size: 27px;
    line-height: 28px;
    text-transform: uppercase;
    letter-spacing: 0.5px;
    color: var(--white);
  }
  .front-web {
    position: absolute;
    left: 46px;
    top: 286px;
    font-size: 15px;
    color: var(--white);
  }
  .front-web strong { color: var(--green); font-weight: 600; }

  /* Back */
  .back-brand {
    position: absolute;
    left: 38px;
    top: 132px;
    display: flex;
    align-items: center;
    gap: 12px;
  }
  .back-brand-dot {
    width: 40px;
    height: 40px;
    border-radius: 50%;
    background: var(--green);
    flex: none;
  }
  .back-brand-name {
    font-weight: 800;
    font-size: 21px;
    line-height: 23px;
    text-transform: uppercase;
    color: var(--white);
  }
  .divider {
    position: absolute;
    left: 298px;
    top: 75px;
    width: 1px;
    height: 191px;
    background: var(--rule);
  }
  .contact {
    position: absolute;
    left: 326px;
    top: 72px;
    font-size: 15px;
    line-height: 21px;
  }
  .contact-name { color: var(--green); font-weight: 700; font-size: 19px; line-height: 24px; }
  .contact-title { margin-bottom: 23px; }
  .contact-company { color: var(--green); font-size: 14.5px; }
  .contact-address { margin-bottom: 6px; }
  .contact-line { display: flex; align-items: center; gap: 6px; line-height: 20px; }
  .contact-line svg { width: 13px; height: 13px; flex: none; }
  .contact-line strong { font-weight: 700; }
  .license {
    position: absolute;
    left: 0;
    right: 0;
    top: 301px;
    text-align: center;
    font-size: 15px;
  }
</style>
</head>
<body>
  <section class="card card--front">
    <div class="front-art-fill" role="img" aria-label="City skyline illustration with a safe combination dial"></div>
    <div class="front-brand">Pinecrest<br>Lockworks</div>
    <div class="front-web">www.<strong>pinecrestlockworks</strong>.com</div>
  </section>

  <section class="card card--back">
    <div class="back-brand">
      <span class="back-brand-dot"></span>
      <span class="back-brand-name">Pinecrest<br>Lockworks</span>
    </div>
    <div class="divider"></div>
    <div class="contact">
      <div class="contact-name">Daniel Whitford</div>
      <div class="contact-title">President</div>
      <div class="contact-company">Pinecrest Lockworks LLC</div>
      <div class="contact-address">1840 Cedar Hollow Rd, Suite 200<br>Fairview , TX , 75069</div>
      <div class="contact-line">
        <svg viewBox="0 0 16 16" aria-hidden="true"><path fill="#1e7a3c" d="M3.6 1.2l2.3 2.4c.4.4.4 1 0 1.4L4.7 6.2c.9 2 2.9 4 5 5l1.2-1.2c.4-.4 1-.4 1.4 0l2.4 2.3c.4.4.4 1 0 1.4l-1.3 1.3c-.6.6-1.5.8-2.3.5C6.3 14 2 9.7.5 4.9.2 4.1.4 3.2 1 2.6L2.2 1.2c.4-.4 1-.4 1.4 0z"/></svg>
        <span>972-555-0146</span>
      </div>
      <div class="contact-line">
        <svg viewBox="0 0 16 16" aria-hidden="true"><rect x="1" y="3" width="14" height="10" fill="none" stroke="#1e7a3c" stroke-width="1.6"/><path d="M1 3.5l7 5.5 7-5.5" fill="none" stroke="#1e7a3c" stroke-width="1.6"/></svg>
        <span>daniel@pinecrestlockworks.com</span>
      </div>
      <div class="contact-line">
        <svg viewBox="0 0 16 16" aria-hidden="true"><g fill="none" stroke="#1e7a3c" stroke-width="1.3"><circle cx="8" cy="8" r="6.5"/><ellipse cx="8" cy="8" rx="3" ry="6.5"/><path d="M1.5 8h13M2.5 4.8h11M2.5 11.2h11"/></g></svg>
        <span>www.<strong>pinecrestlockworks</strong>.com</span>
      </div>
    </div>
    <div class="license">Texas DPS Locksmith License# B10482736</div>
  </section>
</body>
</html>
```